Funeral Insurance Infographic

I need some information about infographic turned into an infographic.

Details are as follows:

Entry Ages: 45 - 70
Expiry age: No expiry age
Minimum Sum Insured: $5,000
Maximum Sum Insured: $10,000
Cooling off period: 30 Days

First two years of policy benefit if not paid if death is caused by suicide

Accidental only covered in first 2 years - no other deaths covered.

All deaths covered after that

Available for Australian residents only

```html
<!DOCTYPE html>
<html lang="en">
<head>
<meta charset="utf-8">
<title>Funeral Insurance Infographic</title>
<link href="https://fonts.googleapis.com/css2?family=Great+Vibes&family=Oswald:wght@500;700&display=swap" rel="stylesheet">
<style>
  :root {
    --page: #e9e9e9;
    --building: #d3d3d3;
    --sky: #8cc6ea;
    --panel: #c2b6a2;
    --brown: #7a5232;
    --tan: #c9a37b;
    --cream: #f4ecdc;
    --ink: #252525;
    --red: #e3201f;
    --orange: #f6a736;
    --yellow: #f4e53c;
    --grass: #8cc43f;
  }
  * { margin: 0; padding: 0; box-sizing: border-box; }
  html, body { width: 925px; height: 1200px; overflow: hidden; background: var(--page); }
  .canvas { position: relative; width: 925px; height: 1200px; overflow: hidden; background: var(--page); font-family: "Oswald", sans-serif; color: var(--ink); }
  .abs { position: absolute; }
  .building { left: 28px; top: 40px; width: 870px; height: 900px; background: var(--building); border-radius: 420px 420px 0 0 / 120px 120px 0 0; }
  .column-left { left: 0; top: 300px; width: 30px; height: 640px; background: var(--sky); }
  .column-right { right: 0; top: 300px; width: 28px; height: 640px; background: var(--sky); }
  .ledge { left: 28px; top: 880px; width: 870px; height: 12px; background: #bdbdbd; }
  .ribbon-tail { top: 135px; width: 190px; height: 150px; background: var(--tan); }
  .ribbon-tail.left { left: 0; clip-path: polygon(0 0, 100% 0, 100% 100%, 0 100%, 28% 50%); }
  .ribbon-tail.right { right: 0; clip-path: polygon(0 0, 100% 0, 72% 50%, 100% 100%, 0 100%); }
  .title-banner { left: 140px; top: 70px; width: 648px; height: 195px; background: var(--brown); box-shadow: 4px 6px 10px rgba(0,0,0,.35); display: flex; flex-direction: column; align-items: center; justify-content: center; }
  .title-banner h1 { font-family: "Great Vibes", cursive; font-weight: 400; color: var(--cream); font-size: 86px; line-height: 78px; text-align: center; }
  .panel { left: 60px; width: 810px; background: var(--panel); box-shadow: 4px 6px 12px rgba(0,0,0,.35); }
  .panel.first { top: 318px; height: 260px; }
  .panel.second { top: 592px; height: 262px; }
  .side-band { width: 60px; height: 300px; background: #8e7e72; }
  .side-band.left { left: 0; top: 318px; clip-path: polygon(0 25%, 100% 0, 100% 70%, 0 100%); }
  .side-band.right { right: 0; top: 560px; clip-path: polygon(0 0, 100% 20%, 100% 100%, 0 75%); }
  .placeholder { border-radius: 4px; }
  .entry-label { left: 92px; top: 455px; width: 220px; text-align: center; font-weight: 700; font-size: 36px; line-height: 38px; }
  .no-expiry { left: 340px; top: 330px; width: 236px; height: 236px; }
  .expiry-word { left: 340px; top: 378px; width: 236px; text-align: center; color: var(--red); font-weight: 700; font-size: 56px; line-height: 62px; }
  .no-expiry-caption { left: 340px; top: 528px; width: 236px; text-align: center; color: #fff; font-size: 12px; font-weight: 700; }
  .range-label { color: var(--red); font-weight: 700; font-size: 34px; }
  .sum-label { left: 650px; top: 400px; width: 80px; text-align: center; font-weight: 700; font-size: 19px; line-height: 26px; }
  .bracket { left: 690px; top: 340px; width: 160px; height: 210px; }
  .tag { background: var(--red); color: #fff; font-size: 13px; font-weight: 700; padding: 2px 6px; border-radius: 2px; }
  .note { left: 120px; top: 590px; width: 190px; height: 192px; background: var(--orange); box-shadow: 4px 6px 10px rgba(0,0,0,.35); text-align: center; clip-path: polygon(0 0, 100% 0, 100% 82%, 86% 100%, 0 100%); }
  .note-curl { left: 284px; top: 748px; width: 26px; height: 34px; background: var(--yellow); clip-path: polygon(100% 0, 0 100%, 0 0); }
  .note .small { font-weight: 700; font-size: 21px; line-height: 24px; margin-top: 6px; }
  .note .mid { font-weight: 700; font-size: 32px; line-height: 34px; }
  .note .big { color: var(--red); font-weight: 700; font-size: 88px; line-height: 84px; }
  .no-pay { left: 448px; top: 660px; font-weight: 700; font-size: 34px; line-height: 60px; }
  .no-pay span { color: var(--red); font-size: 60px; vertical-align: -6px; }
  .caption { font-size: 12.5px; font-weight: 500; line-height: 17px; text-align: center; }
  .closing { left: 220px; top: 968px; width: 470px; text-align: center; font-weight: 700; }
  .closing .lead { font-size: 30px; line-height: 38px; }
  .closing .sub { font-size: 23px; line-height: 32px; }
</style>
</head>
<body>
<main class="canvas">
  <div class="abs building"></div>
  <div class="abs column-left"></div>
  <div class="abs column-right"></div>
  <div class="abs side-band left"></div>
  <div class="abs side-band right"></div>

  <div class="abs ribbon-tail left"></div>
  <div class="abs ribbon-tail right"></div>
  <header class="abs title-banner">
    <h1>Funeral Insurance<br>Infographic</h1>
  </header>

  <section class="abs panel first"></section>
  <div class="abs placeholder" role="img" aria-label="Three black silhouette figures of increasing age" style="left:95px;top:338px;width:210px;height:112px;background:linear-gradient(#2a2a2a,#444);"></div>
  <div class="abs entry-label">45-70 y/o<br>Entry Ages</div>

  <svg class="abs no-expiry" viewBox="0 0 236 236" aria-hidden="true">
    <circle cx="118" cy="118" r="106" fill="none" stroke="#252525" stroke-width="20"/>
  </svg>
  <div class="abs expiry-word">Expiry<br>Age</div>
  <svg class="abs no-expiry" viewBox="0 0 236 236" aria-hidden="true">
    <line x1="190" y1="46" x2="46" y2="190" stroke="#252525" stroke-width="18"/>
  </svg>
  <div class="abs no-expiry-caption">No Expiry Age</div>

  <div class="abs range-label" style="left:632px;top:322px;">MAX</div>
  <div class="abs range-label" style="left:632px;top:498px;">MIN</div>
  <svg class="abs bracket" viewBox="0 0 160 210" aria-hidden="true">
    <g stroke="#252525" stroke-width="12" fill="none">
      <line x1="44" y1="8" x2="44" y2="184"/>
      <line x1="20" y1="8" x2="80" y2="8"/>
      <line x1="20" y1="184" x2="80" y2="184"/>
    </g>
    <ellipse cx="92" cy="8" rx="12" ry="6" fill="none" stroke="#252525" stroke-width="3"/>
    <ellipse cx="92" cy="184" rx="12" ry="6" fill="none" stroke="#252525" stroke-width="3"/>
  </svg>
  <div class="abs tag" style="left:790px;top:343px;">$10000</div>
  <div class="abs tag" style="left:790px;top:515px;">$5000</div>
  <div class="abs sum-label">Sum<br>Insured</div>
  <div class="abs placeholder" role="img" aria-label="Fan of banknotes" style="left:760px;top:375px;width:82px;height:120px;background:linear-gradient(135deg,#6cbf8f,#e8d77a);"></div>

  <section class="abs panel second"></section>
  <div class="abs placeholder" role="img" aria-label="Hourglass with sand running" style="left:64px;top:605px;width:70px;height:178px;background:linear-gradient(#2a2a2a,#d9d2c4 50%,#2a2a2a);"></div>
  <div class="abs note">
    <div class="small">Cooling Off</div>
    <div class="mid">Period</div>
    <div class="big">30</div>
    <div class="mid">DAYS</div>
  </div>
  <div class="abs note-curl"></div>

  <div class="abs placeholder" role="img" aria-label="Red figure under a gallows" style="left:345px;top:600px;width:95px;height:160px;background:linear-gradient(#252525,#c33);"></div>
  <div class="abs no-pay">=NO <span>$</span></div>
  <p class="abs caption" style="left:322px;top:766px;width:245px;">First two years of policy benefit is<br>not paid if death is caused by suicide</p>

  <div class="abs placeholder" role="img" aria-label="Car striking a red pedestrian figure" style="left:592px;top:630px;width:240px;height:105px;background:linear-gradient(90deg,#222 75%,#d62b2b);"></div>
  <p class="abs caption" style="left:585px;top:746px;width:245px;">Accidental only covered in first 2 years<br>- no other deaths covered.</p>

  <div class="abs ledge"></div>

  <div class="abs placeholder" role="img" aria-label="Black tombstone with a white cross" style="left:75px;top:935px;width:135px;height:135px;background:#1f1f1f;border-radius:40px 40px 4px 4px;"></div>
  <div class="abs closing">
    <div class="lead">All deaths covered after that</div>
    <div class="sub">Available for Australian residents only</div>
  </div>
  <div class="abs placeholder" role="img" aria-label="Australian flag" style="left:677px;top:963px;width:158px;height:80px;background:linear-gradient(90deg,#2b3d91,#1f2f7d);box-shadow:3px 5px 8px rgba(0,0,0,.35);"></div>

  <div class="abs" role="img" aria-label="Strip of green grass" style="left:0;top:1100px;width:925px;height:100px;background:linear-gradient(#c7e07a,var(--grass));"></div>
</main>
</body>
</html>
```